Ridgeline Journeys business card

please see website
www.ridgelinejourneys.comau

info needed on card
Kieran Folsby
Ph
email
Adventure Riding GPS trails

please use my logo and colours off my site

Industry/Entity Type

Business

Contact Information for Business Card

Kieran Folsby
kieran@ridgelinejourneys.com

```html
<!DOCTYPE html>
<html lang="en">
<head>
<meta charset="utf-8">
<title>Ridgeline Journeys – Business Card</title>
<link href="https://fonts.googleapis.com/css2?family=Open+Sans:wght@300;400;800&display=swap" rel="stylesheet">
<style>
  :root {
    --bg: #e9e6e1;
    --card-white: #ffffff;
    --card-shade: #eeeeee;
    --brand-yellow: #e4e21e;
    --yellow-soft: #f1f0a6;
    --stripe-black: #1c1c1c;
    --stripe-orange: #f0a020;
    --ink: #1d1d1d;
    --ink-soft: #3a3a3a;
    --mark-grey: #8a8a8a;
  }
  * { margin: 0; padding: 0; box-sizing: border-box; }
  html, body { width: 1200px; height: 892px; overflow: hidden; }
  body {
    background: var(--bg);
    font-family: "Open Sans", Arial, sans-serif;
    display: flex;
    flex-direction: column;
    align-items: center;
    justify-content: center;
    gap: 40px;
  }
  .card {
    position: relative;
    width: 680px;
    height: 390px;
    border-radius: 26px;
    overflow: hidden;
    box-shadow: 0 6px 18px rgba(0,0,0,0.18);
  }
  .card-front { background: radial-gradient(ellipse at 50% 45%, var(--card-white) 55%, var(--card-shade) 100%); }
  .front-bands { position: absolute; inset: 0; }
  .front-content {
    position: absolute;
    left: 130px; right: 130px; top: 52px; bottom: 52px;
    display: grid;
    grid-template-columns: 110px 1fr;
    grid-template-rows: auto 1fr;
    column-gap: 30px;
  }
  .brand-name {
    grid-column: 1 / 3;
    font-weight: 800;
    font-size: 38px;
    line-height: 1;
    text-transform: uppercase;
    color: var(--ink);
    letter-spacing: 0.5px;
    display: flex;
    align-items: center;
    gap: 16px;
    margin-bottom: 34px;
  }
  .brand-dot {
    width: 26px; height: 26px;
    border-radius: 50%;
    background: var(--brand-yellow);
    flex: none;
  }
  .contact { grid-column: 1 / 3; }
  .person-name {
    font-weight: 300;
    font-size: 36px;
    color: var(--ink-soft);
    margin-bottom: 28px;
  }
  .contact-line {
    font-weight: 400;
    font-size: 19px;
    color: var(--ink-soft);
    line-height: 1.45;
  }
  .card-back {
    background: radial-gradient(ellipse at 18% 88%, var(--brand-yellow) 0%, var(--yellow-soft) 38%, var(--card-white) 78%);
    display: flex;
    align-items: center;
    justify-content: center;
    gap: 22px;
  }
  .back-brand {
    font-weight: 800;
    font-size: 50px;
    text-transform: uppercase;
    color: var(--ink);
    letter-spacing: 0.5px;
  }
</style>
</head>
<body>

  <section class="card card-front" aria-label="Business card front">
    <svg class="front-bands" viewBox="0 0 680 390" preserveAspectRatio="none" aria-hidden="true">
      <path d="M0 0 H120 Q40 195 120 390 H0 Z" fill="var(--brand-yellow)"/>
      <path d="M120 0 Q40 195 120 390" fill="none" stroke="var(--stripe-black)" stroke-width="10"/>
      <path d="M132 0 Q52 195 132 390" fill="none" stroke="var(--stripe-orange)" stroke-width="4"/>
      <path d="M680 0 H560 Q640 195 560 390 H680 Z" fill="var(--brand-yellow)"/>
      <path d="M560 0 Q640 195 560 390" fill="none" stroke="var(--stripe-black)" stroke-width="10"/>
      <path d="M548 0 Q628 195 548 390" fill="none" stroke="var(--stripe-orange)" stroke-width="4"/>
    </svg>
    <div class="front-content">
      <div class="brand-name"><span class="brand-dot"></span>Ridgeline Journeys</div>
      <div class="contact">
        <p class="person-name">Kieran Folsby</p>
        <p class="contact-line">kieran@ridgelinejourneys.com</p>
        <p class="contact-line">www.ridgelinejourneys.comau</p>
      </div>
    </div>
  </section>

  <section class="card card-back" aria-label="Business card back">
    <span class="brand-dot"></span>
    <span class="back-brand">Ridgeline Journeys</span>
  </section>

</body>
</html>
```